Professional "Aviation Parts" Auction Website with Customer Login Backend Module

Need an "Aviation Parts" Website with 4 major listing options.
- AUCTION
Seller can list their items on the site as an auction with a small listing fee. Seller has to create an account in order to be able to create or edit a listing. Seller must be able to have a reserve price.
- SELLING
Sellers can list their items with a small listing fee. Imortant is, that Sellers has a back end module, (like lotvane) where they can log in and create or make changes to existing listings.
- BUYING
Buyers can search items either by part number in a search bar, or scroll through categories and subcategories to find the respective part.
- WANTED
Customers should be able to create a “Wanted” listing for items of interest.

In all four cases, customers (Buyers/Seller) must create an account to either place a bid, buy now, create a “wanted” listing or create/edit their own for sale/auction listing. NO login is required to search the website or browse through categories and to see listings. The website should be “Lotvane like” with login module, payment, coinrill connection, etc and easy to navigate. A design example is https://www.skylotra-hub.com/ . I’m open for all ideas.

Target Market(s)

Aviation Industry
Helicopter Industry

Industry/Entity Type

Aviation

Number of Pages Required

5+ page

Font styles to use
Serif
Sans Serif

Colors
85acd3
3176b5
9d9d9d
d3d3d3

Requirements
Must have
• Our company is called Torvinex.com, LLC and is specialized in aviation parts listings. The website must have 4 major options: Auction, Sell, Buy, and Wanted listings. The Buyer/Seller must create an account in order to bid, buy or sell an item. No login is required if someone just wants to browse the website to look for pricing and parts. Once they decide to purchase, they have to login or create an account. The same counts for the seller. Seller must create an account to list a "For Sale", "Auction" or "Wanted" Listing. Each listing requires a small listing fee, which will be charged by us and should be paid via CoinRill. CoinRill should be interfaced as a preferred payment method. Other payment options are available as well. The website idea is very similar to Lotvane. Same style listings as Lotvane and other auction pages. A good design idea is https://www.skylotra-hub.com/ to get a better understanding. The website must be easy to navigate and modern looking with a professional color scheme. The logo is attached. I would like to keep the website in a similar color scheme as the logo design.
• There should be two main Categories on the main page to select from:
• - Helicopter Listings
• - Airplane Listings
• The 1st "Sub-Category" once you click on either one of the top category, will be "Aircraft Make".
• The 2nd "Sub-Category" will be "Aircraft Model".
• The 3rd "Sub-Category" will be "Parts" for that specific aircraft.
• Also there should be a CoinRill interface, if a buyer wants to purchase an item, so they can use their credit card or request wire information from the seller after closing.
• It also has to include an option when a seller lists an item, they will be required to make a payment to us for listing on our website. For example $1.99 for a listing value up to $100. A listing fee for a sale value of up to $1,000 will be $4.99, and so on. Listing fee for up to $10,000 will be $14.99. Listing fee for up to $100.000 will be $49.99. This system is very similar to the Lotvane platform.
Nice to have
• It would be nice to have a easy to maintain back-end module which can easily be manged by our personnel.
Should not have
• The page should not look childish with random colors. A professional appearance and easy to navigate is a must.

```html
<!DOCTYPE html>
<html lang="en">
<head>
<meta charset="utf-8">
<title>Torvinex.com – Aviation Parts</title>
<link href="https://fonts.googleapis.com/css2?family=Exo+2:wght@400;500;600;700&family=Open+Sans:wght@400;600;700&display=swap" rel="stylesheet">
<style>
:root{
  --frame:#e4e4e4;
  --sky:#29abe2;
  --navy:#0b4470;
  --navy-deep:#062c4b;
  --panel:rgba(8,26,44,.88);
  --field:#0a2238;
  --ink:#1f2a36;
  --muted:#5d6670;
  --light-blue:#5db9e6;
  --orange:#f7941d;
  --white:#ffffff;
}
*{box-sizing:border-box;margin:0;padding:0}
html,body{width:1200px;height:2655px;overflow:hidden}
body{background:var(--frame);font-family:"Open Sans",sans-serif;color:var(--ink);position:relative}
.page{position:absolute;left:14px;top:14px;width:1172px;height:2627px;background:linear-gradient(#f6f9fb 0,#eef3f7 40%,#f4f7fa 70%,#fff 100%);overflow:hidden}
.abs{position:absolute}
.heading-font{font-family:"Exo 2",sans-serif}

/* top bar */
.topbar{left:0;top:0;width:1172px;height:46px;background:var(--sky);color:var(--white);font-family:"Exo 2",sans-serif;font-weight:600;font-size:13px;display:flex;align-items:center;padding:0 24px}
.topbar .item{display:flex;align-items:center;gap:8px;margin-right:28px}
.topbar .spacer{flex:1}
.topbar .sep{width:1px;height:18px;background:rgba(255,255,255,.7);margin:0 16px 0 -12px}
.icon-dot{width:18px;height:18px;border-radius:50%;border:2px solid var(--white);display:inline-block}

/* hero */
.hero{left:0;top:46px;width:1172px;height:700px}
.brand{left:24px;top:90px;display:flex;align-items:center;gap:12px}
.brand-mark{width:44px;height:44px;border-radius:50%;background:var(--navy)}
.brand-name{font-family:"Exo 2",sans-serif;font-weight:600;font-size:34px;letter-spacing:2px;color:var(--sky)}
.nav{right:30px;top:96px;display:flex;align-items:center;gap:18px;font-family:"Exo 2",sans-serif;font-weight:600;font-size:13px;color:var(--navy);text-transform:uppercase}
.nav a{display:flex;align-items:center;gap:6px;color:inherit;text-decoration:none}
.nav .ico{width:13px;height:13px;border:2px solid var(--navy);border-radius:2px}
.nav .bar{width:2px;height:24px;background:var(--navy)}

/* parts finder */
.finder{left:103px;top:354px;width:991px;height:296px;background:var(--panel);border:2px solid rgba(255,255,255,.8);border-radius:4px}
.finder-title{left:80px;top:22px;font-family:"Exo 2",sans-serif;font-weight:700;font-size:29px;color:var(--white)}
.finder-title span{color:var(--sky)}
.finder-lens{left:-22px;top:-22px}
.btn-listings{left:725px;top:20px;width:234px;height:30px;background:var(--sky);color:var(--white);font-family:"Exo 2",sans-serif;font-weight:700;font-size:12px;display:flex;align-items:center;justify-content:center;gap:10px}
.finder-inner{left:15px;top:72px;width:957px;height:208px;border:1px solid rgba(255,255,255,.7);border-radius:3px}
.tabs{left:6px;top:6px;width:943px;height:40px;background:#0c1826}
.tab{top:0;height:40px;display:flex;align-items:center;justify-content:center;font-family:"Exo 2",sans-serif;font-size:16px}
.tab-cat{left:0;width:110px;background:#000;color:var(--white);font-weight:600;font-size:14px}
.tab-heli{left:108px;width:218px;color:#000;font-weight:600}
.tab-air{left:300px;width:200px;color:var(--white);font-weight:500}
.part-search{right:8px;top:7px;width:226px;height:26px;background:var(--white);border-radius:13px;display:flex;align-items:center;gap:8px;padding:0 10px;font-size:12px;color:#555}
.label{color:var(--white);font-size:14px;font-weight:600}
.select{height:36px;background:var(--field);color:var(--white);font-size:13px;font-weight:600;display:flex;align-items:center;padding:0 10px;justify-content:space-between}
.caret{width:0;height:0;border-left:7px solid transparent;border-right:7px solid transparent;border-top:8px solid var(--white)}
.btn-search{background:var(--sky);color:var(--white);font-family:"Exo 2",sans-serif;font-weight:700;font-size:15px;display:flex;align-items:center;justify-content:center;gap:10px;height:36px}
.btn-reset{background:#15191d;color:var(--white);font-family:"Exo 2",sans-serif;font-weight:700;font-size:15px;display:flex;align-items:center;justify-content:center;height:36px}

/* featured */
.section-title{display:flex;align-items:center;gap:12px;font-family:"Exo 2",sans-serif;font-weight:600;font-size:23px;color:var(--navy)}
.section-title .accent{color:var(--sky)}
.title-dot{width:46px;height:46px;border-radius:50%;border:3px solid var(--sky)}
.card{top:919px;width:444px;height:407px;background:var(--white);box-shadow:0 2px 8px rgba(0,0,0,.08)}
.card-photo{left:0;top:14px;width:444px;height:253px}
.card-flag{right:-8px;top:0}
.card-flag span{position:absolute;right:18px;top:44px;font-size:11px;color:var(--white);font-weight:600}
.card-title{left:20px;top:283px;font-family:"Exo 2",sans-serif;font-weight:700;font-size:17px;letter-spacing:1px;color:#2b2b2b}
.card-text{left:20px;top:316px;width:410px;font-size:13.5px;line-height:21px;color:var(--ink)}
.card-rule{left:0;bottom:0;width:444px;height:5px;background:linear-gradient(90deg,var(--sky) 0,var(--sky) 30%,var(--navy) 30%,var(--navy) 55%,var(--sky) 55%,var(--sky) 75%,var(--navy) 75%)}
.arrow{width:28px;height:28px;border-radius:50%;background:#8d8d8d;border:2px solid #cfcfcf;display:flex;align-items:center;justify-content:center}

/* about */
.about-title{left:52px;top:1578px;display:flex;align-items:center;gap:14px;font-family:"Exo 2",sans-serif;font-weight:600;font-size:23px;color:var(--white)}
.about-title .title-dot{border-color:var(--white);width:44px;height:44px}
.about-text{left:53px;top:1668px;width:480px;font-size:14px;line-height:22px;color:var(--white)}

/* newsletter */
.news-title{left:0;top:2072px;width:1172px;text-align:center;font-family:"Exo 2",sans-serif;font-weight:600;font-size:24px;color:var(--navy)}
.news-title span{color:var(--sky)}
.news-bar{left:129px;top:2115px;width:914px;height:63px;background:var(--white);border:1px solid #cfd6dd;border-radius:5px;display:flex;align-items:center;padding:0 12px 0 18px;gap:16px}
.news-bar .placeholder{flex:1;font-size:17px;color:#8a8a8a}
.btn-submit{width:148px;height:44px;background:var(--orange);color:var(--white);font-family:"Exo 2",sans-serif;font-weight:600;font-size:18px;border-radius:4px;display:flex;align-items:center;justify-content:center}

/* footer */
.footer{left:87px;top:2271px;width:997px;height:265px;background:var(--light-blue);border-radius:5px}
.footer-brand{left:32px;top:95px;display:flex;align-items:center;gap:12px}
.footer-brand .brand-mark{background:var(--white);width:40px;height:40px}
.footer-brand .brand-name{color:var(--white);font-size:30px}
.socials{left:97px;top:154px;display:flex;gap:5px}
.socials i{width:16px;height:16px;border:1.5px solid var(--white);border-radius:50%;display:block}
.foot-col{top:38px;color:var(--white)}
.foot-col h4{font-family:"Exo 2",sans-serif;font-weight:600;font-size:13px;margin-bottom:34px;text-transform:uppercase}
.foot-col li{list-style:none;font-size:12.5px;font-weight:600;line-height:19.5px}
.support{left:715px;top:36px;width:274px;height:189px;background:var(--navy-deep);border-radius:5px;color:var(--white);text-align:center}
.support .s-title{margin-top:26px;font-family:"Exo 2",sans-serif;font-weight:600;font-size:19px}
.support .s-phone{margin-top:10px;display:flex;justify-content:center;align-items:center;gap:10px;font-family:"Exo 2",sans-serif;font-weight:600;font-size:29px}
.support .s-or{margin-top:14px;font-size:14px;font-weight:700}
.support .s-mail{margin-top:6px;display:flex;justify-content:center;align-items:center;gap:8px;font-size:14px;font-weight:700}
.legal{left:0;top:2568px;width:1172px;height:59px;background:var(--white);display:flex;align-items:center;justify-content:space-between;padding:0 12px 0 20px;font-size:11.5px;font-weight:700;color:#333}
</style>
</head>
<body>
<div class="page">

  <!-- hero visual -->
  <svg class="abs hero" width="1172" height="700" viewBox="0 0 1172 700" role="img" aria-label="Business jet wing and engine against a blue sky">
    <defs>
      <linearGradient id="heroSky" x1="0" y1="0" x2="0" y2="1">
        <stop offset="0" stop-color="#e8f0f7"/>
        <stop offset=".3" stop-color="#b9cfe2"/>
        <stop offset=".6" stop-color="#3c77a9"/>
        <stop offset="1" stop-color="#0d4a7c"/>
      </linearGradient>
    </defs>
    <polygon points="0,0 1172,0 1172,636 676,700 496,700 0,636" fill="url(#heroSky)"/>
  </svg>

  <div class="abs topbar">
    <div class="item"><svg width="18" height="18" viewBox="0 0 18 18"><circle cx="9" cy="9" r="8" fill="none" stroke="#fff" stroke-width="1.6"/><path d="M6 5l2 2-1 1.5c.8 1.3 1.5 2 2.5 2.5L11 10l2 2-1.4 1.4C9 13 5 9 4.6 6.4z" fill="#fff"/></svg>Sales &amp; Support 1.800.555.0148</div>
    <div class="item"><svg width="18" height="18" viewBox="0 0 18 18"><circle cx="9" cy="9" r="8" fill="none" stroke="#fff" stroke-width="1.6"/><rect x="5" y="6" width="8" height="6" fill="none" stroke="#fff" stroke-width="1.3"/><path d="M5 6l4 3 4-3" fill="none" stroke="#fff" stroke-width="1.3"/></svg>info@torvinex.com</div>
    <div class="spacer"></div>
    <div class="item"><svg width="16" height="18" viewBox="0 0 16 18"><rect x="1" y="8" width="14" height="10" rx="1" fill="#fff"/><path d="M4 8V5a4 4 0 0 1 8 0v3" fill="none" stroke="#fff" stroke-width="2"/></svg>SIGN IN</div>
    <div class="sep"></div>
    <div class="item" style="margin-right:0"><svg width="16" height="18" viewBox="0 0 16 18"><circle cx="8" cy="5" r="4" fill="#fff"/><path d="M0 18a8 7 0 0 1 16 0z" fill="#fff"/></svg>CREATE ACCOUNT</div>
  </div>

  <div class="abs brand"><span class="brand-mark"></span><span class="brand-name">TORVINEX</span></div>

  <nav class="abs nav">
    <a><svg width="15" height="14" viewBox="0 0 15 14"><path d="M7.5 0L0 7h2v7h4V9h3v5h4V7h2z" fill="#0b4470"/></svg>Home</a>
    <a><span class="ico"></span>Online Catalog</a>
    <a><span class="ico"></span>Auction</a>
    <a><span class="ico"></span>Selling</a>
    <a><span class="ico"></span>Buying</a>
    <a><span class="ico"></span>Wanted</a>
    <a><svg width="16" height="12" viewBox="0 0 16 12"><rect x="1" y="1" width="14" height="10" fill="none" stroke="#0b4470" stroke-width="1.6"/><path d="M1 1l7 5 7-5" fill="none" stroke="#0b4470" stroke-width="1.6"/></svg>Contact</a>
    <span class="bar"></span>
    <svg width="17" height="17" viewBox="0 0 17 17"><circle cx="7" cy="7" r="5.5" fill="none" stroke="#0b4470" stroke-width="2.2"/><path d="M11 11l5 5" stroke="#0b4470" stroke-width="2.6"/></svg>
  </nav>

  <!-- parts finder -->
  <section class="abs finder">
    <svg class="abs finder-lens" width="80" height="80" viewBox="0 0 80 80"><circle cx="32" cy="32" r="24" fill="#fff" stroke="#111" stroke-width="9"/><path d="M50 50l22 22" stroke="#111" stroke-width="12" stroke-linecap="round"/></svg>
    <div class="abs finder-title">PARTS <span>FINDER</span></div>
    <div class="abs btn-listings"><svg width="26" height="18" viewBox="0 0 26 18"><g fill="#fff"><rect width="4" height="4"/><rect x="7" width="19" height="4"/><rect y="7" width="4" height="4"/><rect x="7" y="7" width="19" height="4"/><rect y="14" width="4" height="4"/><rect x="7" y="14" width="19" height="4"/></g></svg>VIEW ALL LISTINGS</div>
    <div class="abs finder-inner">
      <div class="abs tabs">
        <svg class="abs" style="left:108px;top:0" width="218" height="48" viewBox="0 0 218 48"><polygon points="18,0 218,0 194,40 126,40 118,47 110,40 0,40" fill="#fff"/></svg>
        <div class="abs tab tab-cat">CATEGORY</div>
        <div class="abs tab tab-heli">Helicopter</div>
        <div class="abs tab tab-air">Airplane</div>
        <div class="abs part-search"><svg width="14" height="14" viewBox="0 0 14 14"><circle cx="6" cy="6" r="4.5" fill="none" stroke="#111" stroke-width="1.8"/><path d="M9.5 9.5l3.5 3.5" stroke="#111" stroke-width="2"/></svg>Search by part number</div>
      </div>
      <div class="abs label" style="left:7px;top:71px">Aircraft Make</div>
      <div class="abs select" style="left:7px;top:88px;width:460px">Please select<span class="caret"></span></div>
      <div class="abs label" style="left:487px;top:71px">Aircraft Model</div>
      <div class="abs select" style="left:487px;top:88px;width:460px">Please select<span class="caret"></span></div>
      <div class="abs label" style="left:7px;top:145px">Parts</div>
      <div class="abs select" style="left:7px;top:162px;width:460px">Please select<span class="caret"></span></div>
      <div class="abs btn-search" style="left:485px;top:162px;width:226px"><svg width="20" height="20" viewBox="0 0 20 20"><circle cx="11" cy="8" r="6" fill="none" stroke="#fff" stroke-width="2.4"/><path d="M7 12l-5 6" stroke="#fff" stroke-width="2.8"/></svg>SEARCH</div>
      <div class="abs btn-reset" style="left:722px;top:162px;width:225px">RESET</div>
    </div>
  </section>

  <!-- featured products -->
  <div class="abs section-title" style="left:446px;top:823px"><span class="title-dot"></span><span><span class="accent">Featured</span> Products</span></div>

  <div class="abs arrow" style="left:50px;top:1112px"><svg width="12" height="12" viewBox="0 0 12 12"><path d="M8 1L3 6l5 5" fill="none" stroke="#fff" stroke-width="2.2"/></svg></div>
  <div class="abs arrow" style="left:1093px;top:1112px"><svg width="12" height="12" viewBox="0 0 12 12"><path d="M4 1l5 5-5 5" fill="none" stroke="#fff" stroke-width="2.2"/></svg></div>

  <article class="abs card" style="left:124px">
    <div class="abs card-photo" role="img" aria-label="Jet engine with open cowling in a hangar" style="background:linear-gradient(135deg,#7d8790,#c9c4b8 45%,#4f5a63)"></div>
    <svg class="abs card-flag" width="114" height="114" viewBox="0 0 114 114"><polygon points="0,0 114,0 114,114" fill="#29abe2"/><circle cx="84" cy="22" r="9" fill="none" stroke="#fff" stroke-width="1.6"/><path d="M80 26l8-8M83 18h5v5" fill="none" stroke="#fff" stroke-width="1.6"/></svg>
    <div class="abs card-flag" style="width:114px;height:114px"><span>More Info</span></div>
    <h3 class="abs card-title">PRODUCT #1</h3>
    <p class="abs card-text">Lorem ipsum dolor sit amet, consectetuer adipiscing elit, sed diam nonummy nibh euismod tincidunt ut laoreet do lore magna aliquam erat volutpat.</p>
    <div class="abs card-rule"></div>
  </article>

  <article class="abs card" style="left:604px">
    <div class="abs card-photo" role="img" aria-label="Aircraft landing gear with twin tyres" style="background:linear-gradient(90deg,#2a2c30,#6d7075 35%,#a8a9a6 50%,#6d7075 65%,#2a2c30)"></div>
    <svg class="abs card-flag" width="114" height="114" viewBox="0 0 114 114"><polygon points="0,0 114,0 114,114" fill="#29abe2"/><circle cx="84" cy="22" r="9" fill="none" stroke="#fff" stroke-width="1.6"/><path d="M80 26l8-8M83 18h5v5" fill="none" stroke="#fff" stroke-width="1.6"/></svg>
    <div class="abs card-flag" style="width:114px;height:114px"><span>More Info</span></div>
    <h3 class="abs card-title">PRODUCT #2</h3>
    <p class="abs card-text">Lorem ipsum dolor sit amet, consectetuer adipiscing elit, sed diam nonummy nibh euismod tincidunt ut laoreet do lore magna aliquam erat volutpat.</p>
    <div class="abs card-rule"></div>
  </article>

  <!-- about -->
  <svg class="abs" style="left:0;top:1400px" width="1172" height="620" viewBox="0 0 1172 620">
    <defs>
      <linearGradient id="aboutPhoto" x1="0" y1="0" x2="0" y2="1">
        <stop offset="0" stop-color="#c9d9e8"/>
        <stop offset=".45" stop-color="#8ba0b3"/>
        <stop offset="1" stop-color="#2c3a48"/>
      </linearGradient>
    </defs>
    <polygon points="510,30 1172,0 1172,555 640,605" fill="url(#aboutPhoto)" role="img" aria-label="Technicians inspecting a large jet engine on the apron"/>
    <polygon points="0,30 510,30 640,605 0,545" fill="#0b4470"/>
  </svg>
  <div class="abs about-title"><span class="title-dot"></span>About Torvinex.com, LLC</div>
  <p class="abs about-text">Lorem ipsum dolor sit amet, consectetuer adipiscing elit, sed diam nonummy nibh euismod tincidunt ut laoreet dolore magna aliquam erat volutpat. Ut wisi enim ad minim veniam, quis nostrud exerci ta tion ullamcorper suscipit lobortis nisl ut aliquip ex ea commodo con sequat. Duis autem vel eum iriure dolor in hendrerit in vulputate velit esse molestie consequat, vel illum dolore eu feugiat nulla facilisis at vero eros et accumsan et iusto odio dignissim qui blandit praesent luptatum zzril delenit augue duisdolore te feugait nulla facilisi.</p>

  <!-- newsletter -->
  <h2 class="abs news-title"><span>Stay Connected</span> - Sign up for our email communications</h2>
  <div class="abs news-bar">
    <svg width="26" height="26" viewBox="0 0 26 26"><circle cx="11" cy="11" r="8.5" fill="none" stroke="#222" stroke-width="2.6"/><path d="M17.5 17.5l7 7" stroke="#222" stroke-width="3"/></svg>
    <span class="placeholder">Enter Email Address</span>
    <span class="btn-submit">Submit</span>
  </div>

  <!-- footer -->
  <footer class="abs footer">
    <div class="abs footer-brand"><span class="brand-mark"></span><span class="brand-name">TORVINEX</span></div>
    <div class="abs socials"><i></i><i></i><i></i></div>
    <div class="abs foot-col" style="left:306px">
      <h4>Quick Links</h4>
      <ul><li>Online Catalog</li><li>Auctions</li><li>Selling</li><li>Buying</li><li>Wanted</li><li>Contact</li></ul>
    </div>
    <div class="abs foot-col" style="left:481px">
      <h4>Service &amp; Support</h4>
      <ul><li>Contact Us</li><li>Request/Download Catalog</li><li>Tech Reports</li><li>Supplier Quality Manual</li></ul>
    </div>
    <div class="abs support">
      <div class="s-title">Sales &amp; Support</div>
      <div class="s-phone"><svg width="32" height="32" viewBox="0 0 18 18"><circle cx="9" cy="9" r="8" fill="none" stroke="#fff" stroke-width="1.4"/><path d="M6 5l2 2-1 1.5c.8 1.3 1.5 2 2.5 2.5L11 10l2 2-1.4 1.4C9 13 5 9 4.6 6.4z" fill="#fff"/></svg>1.800.555.0148</div>
      <div class="s-or">or email us</div>
      <div class="s-mail"><svg width="18" height="18" viewBox="0 0 18 18"><circle cx="9" cy="9" r="8" fill="none" stroke="#fff" stroke-width="1.6"/><rect x="5" y="6" width="8" height="6" fill="none" stroke="#fff" stroke-width="1.3"/><path d="M5 6l4 3 4-3" fill="none" stroke="#fff" stroke-width="1.3"/></svg>info@torvinex.com</div>
    </div>
  </footer>

  <div class="abs legal">
    <span>Copyright© 2018 Torvinex.com, LLC. All Rights Reserved.</span>
    <span>Terms &amp; Conditions &nbsp; I &nbsp; Privacy Policy</span>
  </div>
</div>
</body>
</html>
```